New Dental Office Needs an Attractive and user friendly Website Designed

I need a website for a new dental office. The Name is Maplecrest Dentistry. I would like a Modern design with a user friendly interface and usability.
I would like a landing page, a page that lists the services we offer: Cosmetic Dentistry, Implants, Dental Hygiene, Emergency Services, Restorations, Dentures
Target Market(s)
Mid to upper class
Industry/Entity Type
Dentistry
Coding
Coded - Design and coding required
Number of Pages Required
1 page
Requirements
Must have
- Landing page that has a scheduling option, Procedures, operating hours, and contact us info
Nice to have
- Appealing design, Soft comforting colors. Easy to navigate page, Modern and professional.

```html
<!DOCTYPE html>
<html lang="en">
<head>
<meta charset="utf-8">
<title>Maplecrest Dentistry</title>
<link href="https://fonts.googleapis.com/css2?family=Prata&family=Montserrat:wght@400;500;600;700&display=swap" rel="stylesheet">
<style>
:root{
  --teal:#5f8f98;
  --teal-dark:#46737b;
  --teal-soft:#e6f0f1;
  --orange:#e9a121;
  --ink:#2c3538;
  --text:#4f5a5d;
  --muted:#8b9598;
  --white:#ffffff;
  --footer:#2f393c;
  --line:#d9e2e4;
}
*{box-sizing:border-box;margin:0;padding:0}
html,body{width:1200px;height:4628px;overflow:hidden;background:var(--white)}
body{font-family:"Montserrat",sans-serif;color:var(--text);position:relative}
.serif{font-family:"Prata",serif}
.abs{position:absolute}
.btn{position:absolute;display:flex;align-items:center;justify-content:center;gap:8px;border-radius:30px;color:var(--white);font-size:15px;font-weight:600;letter-spacing:.5px;text-transform:uppercase}
.btn-teal{background:var(--teal)}
.btn-orange{background:var(--orange)}
.photo{position:absolute}
.eyebrow{font-size:16px;letter-spacing:3px;color:var(--teal);text-transform:uppercase;font-weight:500}
.para{font-size:19px;line-height:1.62;color:var(--text)}

/* header */
.topbar-phone{left:824px;top:6px;width:260px;height:40px;border-radius:0 0 20px 20px;background:var(--teal);color:var(--white);font-size:15px;font-weight:600;display:flex;align-items:center;justify-content:center;gap:8px}
.logo{left:84px;top:34px;font-family:"Prata",serif;font-size:30px;color:var(--ink);line-height:1}
.nav{left:330px;top:56px;display:flex;gap:36px;font-size:15px;font-weight:600;color:var(--ink);text-transform:uppercase}
.nav .active{color:var(--teal)}
.nav-book{left:1064px;top:48px;width:112px;height:36px;font-size:13px}

/* hero */
.hero-photo{left:0;top:0;width:1200px;height:740px;background:linear-gradient(100deg,#f4f6f6 0%,#eef1f1 38%,#d8cfc6 60%,#b99782 80%,#e8e4df 100%)}
.hero-title{left:112px;top:228px;font-size:68px;line-height:1.05;color:var(--teal-dark)}
.hero-title b{font-weight:400;color:var(--ink)}
.hero-sub{left:112px;top:452px;font-size:18px;color:var(--text)}
.hero-btn1{left:112px;top:494px;width:156px;height:44px}
.hero-btn2{left:292px;top:494px;width:164px;height:44px}

.card{position:absolute;text-align:center;padding:112px 30px 0}
.card h3{font-family:"Prata",serif;font-weight:400;font-size:24px;text-transform:uppercase;margin-bottom:14px}
.card p{font-size:14px;line-height:1.5}
.card .icon{position:absolute;left:50%;width:84px;height:84px;margin-left:-42px;border-radius:50%;display:flex;align-items:center;justify-content:center}
.card-book{left:112px;top:680px;width:336px;height:240px;background:#7fa3aa;color:var(--white)}
.card-book .icon{top:-4px;background:var(--white)}
.card-services{left:448px;top:640px;width:336px;height:288px;background:var(--orange);color:var(--white);border-radius:0 0 60px 0;padding-top:146px}
.card-services .icon{top:-18px;background:var(--orange);border:6px solid var(--white)}
.card-why{left:784px;top:680px;width:336px;height:240px;background:#f2f4f4;color:var(--ink)}
.card-why .icon{top:-4px;background:var(--white);border:2px solid var(--line)}

/* about */
.about-ring{left:80px;top:1050px;width:520px;height:520px;border-radius:50%;border:14px solid #b9ccd0}
.about-photo{left:104px;top:1074px;width:472px;height:472px;border-radius:50%;background:radial-gradient(circle at 50% 40%,#f1d9cb 0%,#c9a797 45%,#5f8f98 100%)}
.about-eyebrow{left:628px;top:1032px}
.about-title{left:628px;top:1062px;font-size:52px;line-height:1.1;color:var(--ink);width:520px}
.about-title span{color:var(--teal-dark)}
.about-text{left:628px;top:1208px;width:534px}
.about-btn{left:628px;top:1480px;width:168px;height:46px}

/* services */
.services-band{left:0;top:1620px;width:1200px;height:790px;background:linear-gradient(180deg,var(--white) 0%,var(--teal-soft) 100%)}
.section-title{position:absolute;left:0;width:1200px;text-align:center;font-family:"Prata",serif;font-size:52px;color:var(--ink)}
.tile{position:absolute;width:324px;height:248px;overflow:hidden}
.tile .photo{left:0;top:0;width:100%;height:100%}
.tile .label{position:absolute;left:0;bottom:0;width:100%;height:46px;background:rgba(95,143,152,.92);color:var(--white);font-size:17px;font-weight:600;text-transform:uppercase;display:flex;align-items:center;justify-content:center}
.tile-feature{background:var(--orange);color:var(--white);text-align:center;padding-top:40px}
.tile-feature h4{font-size:18px;font-weight:600;text-transform:uppercase;margin-bottom:12px}
.tile-feature p{font-size:14px;line-height:1.5;padding:0 40px}
.tile-feature .btn{left:72px;top:164px;width:180px;height:40px;background:var(--teal)}

/* testimonials */
.testi{position:absolute;background:var(--white);border:1px solid var(--line);box-shadow:0 6px 24px rgba(0,0,0,.06)}
.testi-side{top:2660px;width:310px;height:270px;padding:26px 30px;font-size:12px;line-height:1.6;color:var(--muted)}
.testi-main{left:318px;top:2614px;width:564px;height:348px;background:#eef4f5;border:none;text-align:center;padding:96px 48px 0}
.testi-main p{font-size:19px;line-height:1.5;color:var(--ink)}
.testi-main .name{font-family:"Prata",serif;font-size:22px;margin-top:14px;color:var(--ink)}
.avatar{position:absolute;left:244px;top:-28px;width:76px;height:76px;border-radius:50%;background:radial-gradient(circle at 50% 45%,#e8c8b3,#9c7764);border:4px solid var(--white)}
.arrow{position:absolute;top:2770px;width:40px;height:40px;border-radius:50%;background:var(--orange);display:flex;align-items:center;justify-content:center}

/* why */
.why-band{left:0;top:3040px;width:1200px;height:560px;background:linear-gradient(90deg,var(--teal-soft) 0%,#f4f8f8 60%,var(--white) 100%)}
.why-eyebrow{left:112px;top:3140px}
.why-title{left:112px;top:3170px;font-size:52px;color:var(--ink)}
.why-title span{color:var(--teal-dark)}
.why-text{left:112px;top:3260px;width:500px}
.why-ring{left:606px;top:3060px;width:600px;height:560px;border-radius:50%;border:14px solid var(--orange)}
.why-photo{left:624px;top:3078px;width:564px;height:524px;border-radius:50%;background:radial-gradient(circle at 40% 45%,#f2dccf 0%,#bfa193 40%,#7ea6b4 75%,#5f8f98 100%)}

/* contact */
.contact-title{left:130px;top:3718px;font-size:48px;color:var(--ink)}
.contact-item{position:absolute;left:130px;display:flex;gap:22px}
.contact-item svg{flex:none;margin-top:4px}
.contact-item h5{font-size:19px;font-weight:500;color:var(--ink);margin-bottom:4px}
.contact-item p{font-size:17px;line-height:1.45}
.contact-rule{position:absolute;left:130px;width:380px;height:1px;background:var(--line)}
.booking{left:612px;top:3700px;width:516px;height:462px;background:var(--orange);border-radius:0 60px 0 60px;padding:40px 38px}
.booking h3{font-size:22px;letter-spacing:3px;font-weight:600;color:var(--white);text-transform:uppercase;margin-bottom:24px}
.field{position:absolute;background:var(--white);height:54px;display:flex;align-items:center;gap:10px;padding-left:18px;font-size:14px;color:var(--muted)}
.send{left:76px;top:374px;width:364px;height:50px;background:var(--footer);border-radius:4px;font-size:16px}

/* footer */
.footer{left:0;top:4220px;width:1200px;height:408px;background:var(--footer);color:#c6cdcf}
.foot-logo{left:130px;top:4300px;font-family:"Prata",serif;font-size:32px;color:var(--white)}
.social{position:absolute;top:4380px;width:28px;height:28px;border-radius:50%;background:#56646a}
.social.lead{background:var(--orange)}
.foot-col{position:absolute;top:4280px}
.foot-col h6{font-size:16px;font-weight:600;letter-spacing:2px;color:var(--white);text-transform:uppercase;margin-bottom:18px}
.foot-col li{list-style:none;font-size:14px;line-height:2}
.foot-col .bar{position:absolute;left:-22px;top:0;width:2px;height:180px;background:#55636a}
.foot-bottom{left:130px;top:4578px;width:940px;display:flex;justify-content:space-between;font-size:13px;color:#97a2a5;border-top:1px solid #46535a;padding-top:14px}
</style>
</head>
<body>

<!-- hero -->
<div class="photo hero-photo" role="img" aria-label="Smiling couple embracing in a bright home, photograph"></div>
<div class="abs topbar-phone">
  <svg width="14" height="14" viewBox="0 0 24 24"><path fill="#fff" d="M6.6 10.8a15 15 0 0 0 6.6 6.6l2.2-2.2a1 1 0 0 1 1-.25 11.4 11.4 0 0 0 3.6.57 1 1 0 0 1 1 1V20a1 1 0 0 1-1 1A17 17 0 0 1 3 4a1 1 0 0 1 1-1h3.5a1 1 0 0 1 1 1c0 1.25.2 2.45.57 3.57a1 1 0 0 1-.25 1z"/></svg>
  CALL US (+1 555) 014 2290
</div>
<div class="abs logo">Maplecrest<br><span style="font-size:18px;letter-spacing:5px">DENTISTRY</span></div>
<nav class="abs nav"><span class="active">Home</span><span>About</span><span>Services</span><span>Treatments</span><span>Reviews</span><span>Contact Us</span></nav>
<div class="btn btn-orange nav-book">Book Now</div>

<h1 class="abs hero-title serif" style="font-weight:400">We Provide<br><b>Exceptional<br>Dental Care</b></h1>
<p class="abs hero-sub">Lorem ipsum dolor sit amet consectetur adipisci</p>
<div class="btn btn-teal hero-btn1">Book Now ›</div>
<div class="btn btn-orange hero-btn2">View Services ›</div>

<div class="card card-book">
  <div class="icon"><svg width="40" height="40" viewBox="0 0 24 24" fill="none" stroke="#5f8f98" stroke-width="1.6"><rect x="3" y="5" width="18" height="16" rx="2"/><path d="M3 10h18M8 3v4M16 3v4"/></svg></div>
  <h3>Book Appointment</h3>
  <p>Lorem ipsum dolor sit amet, consectetur adipiscing elit, sed do eiusmod</p>
</div>
<div class="card card-services">
  <div class="icon"><svg width="38" height="38" viewBox="0 0 24 24" fill="none" stroke="#fff" stroke-width="1.6"><circle cx="12" cy="12" r="8"/><path d="M12 8v8M8 12h8"/></svg></div>
  <h3>Our Services</h3>
  <p>Lorem ipsum dolor sit amet, consectetur adipiscing elit, sed do eiusmod</p>
</div>
<div class="card card-why">
  <div class="icon"><svg width="36" height="36" viewBox="0 0 24 24" fill="none" stroke="#5f8f98" stroke-width="1.8"><path d="M5 12l5 5 9-10"/></svg></div>
  <h3>Why Choose Us</h3>
  <p>Lorem ipsum dolor sit amet, consectetur adipiscing elit, sed do eiusmod</p>
</div>

<!-- about -->
<div class="abs about-ring"></div>
<div class="photo about-photo" role="img" aria-label="Patient smiling in dental chair during a check-up, photograph"></div>
<div class="abs eyebrow about-eyebrow">Who We Are</div>
<h2 class="abs about-title serif" style="font-weight:400"><span>About</span> Maplecrest Dentistry</h2>
<p class="abs para about-text">Lorem ipsum dolor sit amet, consectetur adipiscing elit, sed do eiusmod tempor incididunt ut labore et dolore magna aliqua. Ut enim ad minim veniam, quis nostrud exercitation ullamco laboris nisi ut aliquip ex ea commodo consequat. Duis aute irure dolor in reprehenderit in voluptate velit esse cillum dolore eu fugiat nulla pariatur. Excepteur sint occaecat cupidatat non proident, sunt in culpa qui officia deserunt mollit anim id est laborum.</p>
<div class="btn btn-teal about-btn">Learn More ›</div>

<!-- services -->
<div class="abs services-band"></div>
<h2 class="section-title" style="top:1680px;font-weight:400">Our Services</h2>

<div class="tile" style="left:96px;top:1800px"><div class="photo" role="img" aria-label="Cosmetic dentistry treatment, photograph" style="background:linear-gradient(135deg,#e9c6c8,#b88f96)"></div><div class="label">Cosmetic Dentistry</div></div>
<div class="tile tile-feature" style="left:438px;top:1800px">
  <h4>Implants</h4>
  <p>Lorem ipsum dolor sit amet, consectetur adipiscing elit, sed do eiusmod tempor incididunt ut</p>
  <div class="btn">Book Appointment ›</div>
</div>
<div class="tile" style="left:780px;top:1800px"><div class="photo" role="img" aria-label="Smiling woman after dental hygiene visit, photograph" style="background:linear-gradient(135deg,#d8e2e3,#a8b9bb)"></div><div class="label">Dental Hygiene</div></div>
<div class="tile" style="left:96px;top:2080px"><div class="photo" role="img" aria-label="Man with toothache, photograph" style="background:linear-gradient(135deg,#9fb6c0,#5a6e78)"></div><div class="label">Emergency Services</div></div>
<div class="tile" style="left:438px;top:2080px"><div class="photo" role="img" aria-label="Close-up of dental restoration, photograph" style="background:linear-gradient(135deg,#e3b0a6,#b9675c)"></div><div class="label">Restorations</div></div>
<div class="tile" style="left:780px;top:2080px"><div class="photo" role="img" aria-label="Set of dentures, photograph" style="background:linear-gradient(135deg,#eadfd6,#c7a99a)"></div><div class="label">Dentures</div></div>

<!-- testimonials -->
<h2 class="section-title" style="top:2490px;font-weight:400">What Patient Says</h2>
<div class="testi testi-side" style="left:120px">Our visit felt calm from the first moment. The team explained every step, the clinic was spotless and the front desk made booking simple. We could not be happier with the care and the friendly smiles we received.</div>
<div class="testi testi-side" style="left:770px">Booking was quick and the staff was kind and patient with my kids. The cleaning was gentle, the results look great, and we left with a clear plan for the next visit. Highly recommended to every family.</div>
<div class="testi testi-main">
  <div class="avatar" role="img" aria-label="Reviewer portrait photograph"></div>
  <p>Lorem ipsum dolor sit amet, consectetur adipiscing elit, sed do eiusmod tempor incididunt ut labore et dolore magna aliqua. Ut enim ad minim veniam, quis nostrud exercitation ullamco laboris nisi ut aliquip ex ea commodo consequat Duis aute irur</p>
  <div class="name">Ellis Warren</div>
  <svg width="120" height="22" viewBox="0 0 120 22" style="margin-top:6px"><g fill="#e9a121"><path id="st" d="M11 1l3 6.5 7 .8-5.2 4.7 1.5 7L11 16.5 4.7 20l1.5-7L1 8.3l7-.8z"/><use href="#st" x="24"/><use href="#st" x="48"/><use href="#st" x="72"/><use href="#st" x="96"/></g></svg>
</div>
<div class="arrow" style="left:56px"><svg width="14" height="14" viewBox="0 0 24 24"><path d="M15 4l-8 8 8 8" stroke="#fff" stroke-width="3" fill="none"/></svg></div>
<div class="arrow" style="left:1104px"><svg width="14" height="14" viewBox="0 0 24 24"><path d="M9 4l8 8-8 8" stroke="#fff" stroke-width="3" fill="none"/></svg></div>

<!-- why choose us -->
<div class="abs why-band"></div>
<div class="abs eyebrow why-eyebrow">Who We Are</div>
<h2 class="abs why-title serif" style="font-weight:400"><span>Why</span> Choose Us</h2>
<p class="abs para why-text">Lorem ipsum dolor sit amet, consectetur adipiscing elit, sed do eiusmod tempor incididunt ut labore et dolore magna aliqua. Ut enim ad minim veniam, quis nostrud exercitation ullamco laboris nisi ut aliquip ex ea commodo consequat. Duis aute irure dolor in reprehenderit in voluptate velit esse cillum dolore eu fugiat nulla pariatur. Excepteur sint occaecat</p>
<div class="abs why-ring"></div>
<div class="photo why-photo" role="img" aria-label="Dentist treating a smiling patient, photograph"></div>

<!-- contact -->
<h2 class="abs contact-title serif" style="font-weight:400">Contact us</h2>
<div class="contact-item" style="top:3810px">
  <svg width="20" height="26" viewBox="0 0 24 30"><path fill="#5f8f98" d="M12 0a10 10 0 0 0-10 10c0 7.5 10 20 10 20s10-12.5 10-20A10 10 0 0 0 12 0zm0 14a4 4 0 1 1 0-8 4 4 0 0 1 0 8z"/></svg>
  <div><h5>Address</h5><p>48 Linden Avenue - Suite 210<br>Brookhaven, Oregon 97401</p></div>
</div>
<div class="contact-rule" style="top:3912px"></div>
<div class="contact-item" style="top:3940px">
  <svg width="22" height="22" viewBox="0 0 24 24"><path fill="#5f8f98" d="M6.6 10.8a15 15 0 0 0 6.6 6.6l2.2-2.2a1 1 0 0 1 1-.25 11.4 11.4 0 0 0 3.6.57 1 1 0 0 1 1 1V20a1 1 0 0 1-1 1A17 17 0 0 1 3 4a1 1 0 0 1 1-1h3.5a1 1 0 0 1 1 1c0 1.25.2 2.45.57 3.57a1 1 0 0 1-.25 1z"/></svg>
  <div><h5>Phone</h5><p>555.301.4820</p></div>
</div>
<div class="contact-rule" style="top:4018px"></div>
<div class="contact-item" style="top:4044px">
  <svg width="22" height="18" viewBox="0 0 24 18"><rect x="1" y="1" width="22" height="16" rx="2" fill="none" stroke="#5f8f98" stroke-width="2"/><path d="M2 2l10 8 10-8" fill="none" stroke="#5f8f98" stroke-width="2"/></svg>
  <div><h5>Email address</h5><p>info@maplecrestdentistry.com</p></div>
</div>

<div class="abs booking">
  <h3>Book Appointment</h3>
  <div class="field" style="left:38px;top:100px;width:214px">First Name</div>
  <div class="field" style="left:264px;top:100px;width:214px">Last Name</div>
  <div class="field" style="left:38px;top:166px;width:214px">Email address</div>
  <div class="field" style="left:264px;top:166px;width:214px">Phone</div>
  <div class="field" style="left:38px;top:232px;width:440px;height:112px;align-items:flex-start;padding-top:16px">Message</div>
  <div class="btn send">Send Message ➔</div>
</div>

<!-- footer -->
<div class="abs footer"></div>
<div class="abs foot-logo">Maplecrest<br><span style="font-size:18px;letter-spacing:5px">DENTISTRY</span></div>
<div class="social lead" style="left:152px"></div>
<div class="social" style="left:192px"></div>
<div class="social" style="left:232px"></div>
<div class="social" style="left:272px"></div>

<div class="foot-col" style="left:430px"><div class="bar"></div><h6>Navigation</h6><ul><li>Home</li><li>About</li><li>Services</li><li>Treatments</li><li>Fees</li></ul></div>
<div class="foot-col" style="left:640px"><div class="bar"></div><h6>Resources</h6><ul><li>Book Appointment</li><li>Terms of Use</li><li>Privacy Policy</li><li>Reviews</li><li>Contact</li></ul></div>
<div class="foot-col" style="left:870px"><div class="bar"></div><h6>Get In Touch</h6><ul><li>90 Alder Road, Brookhaven,<br>OR 97401 USA</li><li>(+1 555) 014 2290</li><li>hello@maplecrestdentistry.com</li></ul></div>

<div class="abs foot-bottom"><span>© 2021 Maplecrest Dentistry. All Rights Reserved</span><span>Terms of use &nbsp;&nbsp; Privacy Policy &nbsp;&nbsp; Sitemap</span></div>

</body>
</html>
```